Quokka Kitchen logo

I am a catering and food business that requires a logo for my website and all related business branding. I also need a label for my hot sauce. You can find my information on Facebook and there is a picture of the logo I currently use and also a bottle of my hot sauce.
I am based in the Adelaide Hills in South Australia. I would like to use black and gold or Purple and gold my colour scheme and really like the hornet cartoon that I currently use. Something more refined and original would be great...
Industry/Entity Type
Catering
Look and feel
Each slider illustrates characteristics of the customer's brand and the style your logo design should communicate.

```html
<!DOCTYPE html>
<html lang="en">
<head>
<meta charset="utf-8">
<title>Quokka Kitchen – Sauce Labels and Logos</title>
<link rel="stylesheet" href="https://fonts.googleapis.com/css2?family=Chakra+Petch:wght@700&family=Oswald:wght@400;500&family=Barlow+Condensed:wght@500;600&display=swap">
<style>
:root{
  --paper:#e3e3e3;
  --paper-dark:#cfcfcf;
  --sauce-red:#b41f1f;
  --ink-black:#131313;
  --gold:#f1c419;
  --chilli-red:#c3282b;
  --white:#ffffff;
  --caption:#111111;
  --swirl:#8a2218;
}
*{margin:0;padding:0;box-sizing:border-box}
html,body{width:1200px;height:1000px;overflow:hidden;background:#fff}
.sheet{position:relative;width:1200px;height:1000px}
.label{position:absolute;top:60px;width:317px;height:600px;overflow:hidden;
  background:radial-gradient(circle at 40% 30%,var(--paper) 0%,var(--paper-dark) 100%)}
.label--red{left:61px}
.label--gold{left:440px}
.label--crimson{left:818px}
.label__band{position:absolute;left:0;top:0;width:317px;height:600px}
.label--red .band-fill{fill:var(--sauce-red)}
.label--gold .band-fill,.label--crimson .band-fill{fill:var(--ink-black)}
.label__swirl{position:absolute;left:0;top:0}
.brand-seal{position:absolute;left:122px;top:28px;width:74px;height:74px;border:2px solid var(--ink-black);border-radius:50%;
  display:flex;align-items:center;justify-content:center;text-align:center;
  font-family:"Oswald",sans-serif;font-weight:500;font-size:11px;line-height:1.1;color:var(--ink-black);text-transform:uppercase}
.label__content{position:absolute;left:0;top:0;width:317px;text-align:center;color:var(--white)}
.tagline{position:absolute;top:183px;width:100%;font-family:"Barlow Condensed",sans-serif;font-weight:500;font-size:13px;letter-spacing:1.5px;text-transform:uppercase}
.product-name{position:absolute;top:199px;width:100%;font-family:"Chakra Petch",sans-serif;font-weight:700;font-size:50px;line-height:43px;letter-spacing:2px;color:var(--white)}
.descriptor{position:absolute;top:294px;left:58px;width:201px;font-family:"Oswald",sans-serif;font-weight:500;font-size:12.5px;line-height:18px;text-transform:uppercase;padding-bottom:4px;border-bottom:1px solid}
.descriptor__big{font-size:15px}
.ingredients{position:absolute;left:85px;top:354px;width:147px;height:77px;border:1px solid;padding:6px 4px;
  font-family:"Barlow Condensed",sans-serif;font-weight:500;font-size:8.5px;line-height:11px;color:var(--white)}
.ingredients__volume{display:block;margin-top:9px;font-family:"Oswald",sans-serif;font-size:12px}
.origin{position:absolute;top:446px;width:100%;font-family:"Oswald",sans-serif;font-weight:500;font-size:11px;line-height:14px;text-transform:uppercase}
.footer{position:absolute;left:28px;top:536px;display:flex;align-items:center;gap:6px;
  font-family:"Oswald",sans-serif;font-weight:500;font-size:9.5px;color:var(--ink-black);text-transform:uppercase}
.footer__seal{width:38px;height:38px;border:1.5px solid var(--ink-black);border-radius:50%;display:flex;align-items:center;justify-content:center;text-align:center;font-size:6px;line-height:1.1}
/* colour schemes */
.label--red .tagline{color:var(--gold)}
.label--red .descriptor{color:var(--white);border-color:var(--gold)}
.label--red .ingredients{border-color:var(--gold)}
.label--red .origin{color:var(--white)}
.label--gold .tagline,.label--gold .descriptor,.label--gold .origin{color:var(--gold)}
.label--gold .descriptor,.label--gold .ingredients{border-color:var(--gold)}
.label--crimson .tagline,.label--crimson .descriptor,.label--crimson .origin{color:var(--chilli-red)}
.label--crimson .descriptor{border-color:var(--chilli-red)}
.label--crimson .ingredients{border-color:#7a6a2a}
.caption{position:absolute;font-family:Arial,Helvetica,sans-serif;font-size:19px;color:var(--caption)}
.logo-mark{position:absolute;border:2.5px solid var(--ink-black);border-radius:50%;display:flex;align-items:center;justify-content:center;flex-direction:column;
  font-family:"Oswald",sans-serif;font-weight:500;color:var(--ink-black);text-transform:uppercase;text-align:center}
.logo-mark--one{left:599px;top:756px;width:165px;height:165px;font-size:22px;line-height:1.15}
.logo-mark--two{left:963px;top:747px;width:184px;height:184px;font-size:24px;line-height:1.15}
</style>
</head>
<body>
<main class="sheet">

  <!-- label version one -->
  <section class="label label--red">
    <svg class="label__band" viewBox="0 0 317 600" aria-hidden="true">
      <path class="band-fill" d="M0 152 L14 147 L30 150 L48 144 L66 149 L88 143 L110 148 L134 142 L158 147 L182 141 L206 146 L230 140 L254 145 L278 139 L300 143 L317 140 L317 512 L298 507 L276 513 L252 508 L226 515 L200 510 L176 516 L150 511 L124 517 L98 512 L72 518 L46 513 L22 518 L0 514 Z"/>
    </svg>
    <div class="brand-seal">Quokka<br>Kitchen</div>
    <div class="label__content">
      <p class="tagline">Southern Australia's Finest</p>
      <h1 class="product-name">QUOKKA<br>SAUCE</h1>
      <p class="descriptor">Hot sauce, marinade, condiment<br><span class="descriptor__big">&amp; extreme flavour bringer</span></p>
      <p class="ingredients">INGREDIENTS: CAPSICUM, WATER, VINEGAR, SUGAR, GARLIC, LEMON JUICE, OLIVE OIL, CHILLI, SPICES, CORNSTARCH, ALMOND, SALT.<span class="ingredients__volume">250 ML</span></p>
      <p class="origin">Product of Australia<br>Best before: Feb. 2013</p>
    </div>
    <div class="footer"><span class="footer__seal">Quokka<br>Kitchen</span>48 Orchard Lane. Hillcrest, S.A. 5999</div>
  </section>

  <!-- label version two -->
  <section class="label label--gold">
    <svg class="label__band" viewBox="0 0 317 600" aria-hidden="true">
      <path class="band-fill" d="M0 150 L16 144 L34 148 L52 142 L72 147 L94 141 L118 146 L140 140 L164 145 L188 139 L212 144 L236 138 L260 143 L282 137 L302 141 L317 137 L317 514 L296 509 L274 515 L250 510 L224 517 L198 512 L174 518 L148 513 L122 519 L96 514 L70 520 L44 515 L20 520 L0 516 Z"/>
      <path d="M120 145 C170 200 175 260 150 320 C125 380 190 430 225 515 L270 512 C230 430 175 380 195 320 C220 250 215 190 170 145 Z" fill="var(--swirl)" opacity="0.55"/>
    </svg>
    <div class="brand-seal">Quokka<br>Kitchen</div>
    <div class="label__content">
      <p class="tagline">Southern Australia's Finest</p>
      <h1 class="product-name">QUOKKA<br>SAUCE</h1>
      <p class="descriptor">Hot sauce, marinade, condiment<br><span class="descriptor__big">&amp; extreme flavour bringer</span></p>
      <p class="ingredients">INGREDIENTS: CAPSICUM, WATER, VINEGAR, SUGAR, GARLIC, LEMON JUICE, OLIVE OIL, CHILLI, SPICES, CORNSTARCH, ALMOND, SALT.<span class="ingredients__volume">250 ML</span></p>
      <p class="origin">Product of Australia<br>Best before: Feb. 2013</p>
    </div>
    <div class="footer"><span class="footer__seal">Quokka<br>Kitchen</span>48 Orchard Lane. Hillcrest, S.A. 5999</div>
  </section>

  <!-- label version three -->
  <section class="label label--crimson">
    <svg class="label__band" viewBox="0 0 317 600" aria-hidden="true">
      <path class="band-fill" d="M0 142 L18 138 L38 141 L58 136 L80 140 L102 134 L126 139 L150 133 L174 138 L198 132 L222 137 L246 131 L270 136 L292 130 L317 134 L317 512 L296 507 L272 513 L248 508 L222 515 L196 510 L172 516 L146 511 L120 517 L94 512 L68 518 L42 513 L18 518 L0 514 Z"/>
    </svg>
    <div class="brand-seal">Quokka<br>Kitchen</div>
    <div class="label__content">
      <p class="tagline">Southern Australia's Finest</p>
      <h1 class="product-name">QUOKKA<br>SAUCE</h1>
      <p class="descriptor">Hot sauce, marinade, condiment<br><span class="descriptor__big">&amp; extreme flavour bringer</span></p>
      <p class="ingredients">INGREDIENTS: CAPSICUM, WATER, VINEGAR, SUGAR, GARLIC, LEMON JUICE, OLIVE OIL, CHILLI, SPICES, CORNSTARCH, ALMOND, SALT.<span class="ingredients__volume">250 ML</span></p>
      <p class="origin">Product of Australia<br>Best before: Feb. 2013</p>
    </div>
    <div class="footer"><span class="footer__seal">Quokka<br>Kitchen</span>48 Orchard Lane. Hillcrest, S.A. 5999</div>
  </section>

  <p class="caption" style="left:61px;top:686px">label v.1</p>
  <p class="caption" style="left:440px;top:686px">label v.2</p>
  <p class="caption" style="left:818px;top:686px">label v.3</p>

  <div class="logo-mark logo-mark--one">Quokka<br>Kitchen</div>
  <div class="logo-mark logo-mark--two">Quokka<br>Kitchen</div>

  <p class="caption" style="left:642px;top:948px">logo v.1</p>
  <p class="caption" style="left:1017px;top:948px">logo v.2</p>

</main>
</body>
</html>
```